A5 Flyer for Financial Services Business

I am after a re-design of our business flyer to fit in with our new branding style and logo colour scheme. Wanting something with a bit of designer flair that I could not create myself. I have included the flyer which I created which lacks style so dazzle me.

I want to use the same content.

Text for main body of flyer is

Are you a small business owner, tradie or PAVC Service Provider struggling to stay on top of your bookkeeping and compliance obligations? If so we would love to help you get back on track and take control of your business finances so that you can make informed business decisions and focus on what you do best.

We have over 20 years industry experience and, as a small business ourselves, we are able to offer our clients a personal bookkeeping solution tailored to meet the needs of your business.

Accounts Payable | Accounts Receivable
Customer Invoicing
Bank and Credit Card Reconciliations
Payroll | Superannuation | Payroll Tax
Business Activity | Instalment Activity Statements
Regular Financial Reports
Ledgerly and Bookwise Set-Up and Training

```html
<!DOCTYPE html>
<html lang="en">
<head>
<meta charset="utf-8">
<title>Even Keel Ledger Services – Bookkeeping Flyer</title>
<link href="https://fonts.googleapis.com/css2?family=Montserrat:wght@600;700;800&family=Open+Sans:wght@300;400&display=swap" rel="stylesheet">
<style>
  :root {
    --teal: #17a8a2;
    --teal-text: #1a9f9a;
    --navy: #1c4a6b;
    --ink: #444a4d;
    --white: #ffffff;
    --backdrop: #d4d4d4;
    --photo-light: #b8b3ad;
    --photo-dark: #5e5955;
  }
  * { margin: 0; padding: 0; box-sizing: border-box; }
  html, body { width: 1200px; height: 840px; overflow: hidden; }
  body { background: var(--backdrop); position: relative; font-family: "Open Sans", Arial, sans-serif; }

  .flyer {
    position: absolute; left: 317px; top: 20px;
    width: 566px; height: 800px;
    background: var(--white); overflow: hidden;
    box-shadow: 0 6px 18px rgba(0,0,0,.18);
  }
  .flyer-art { position: absolute; inset: 0; }

  .brand {
    position: absolute; right: 20px; top: 28px;
    text-align: right; color: var(--navy);
    font-family: "Open Sans", Arial, sans-serif; font-weight: 400;
    font-size: 13px; line-height: 1.25; letter-spacing: .5px;
  }
  .brand-mark { display: block; width: 30px; height: 30px; background: var(--navy); margin: 0 0 8px auto; }

  .headline {
    position: absolute; right: 20px; top: 150px; text-align: right;
    color: var(--white); font-family: "Montserrat", Arial, sans-serif;
  }
  .headline-top { display: block; font-weight: 800; font-size: 31px; line-height: 1; letter-spacing: .5px; }
  .headline-main { display: block; font-weight: 800; font-size: 46px; line-height: 1.05; letter-spacing: .5px; }
  .headline-sub { display: block; font-weight: 600; font-size: 14px; letter-spacing: 2.6px; margin-top: 2px; }

  .credentials {
    position: absolute; left: 368px; top: 262px; width: 210px; height: 57px;
    border: 2px solid var(--white); border-right: none; border-radius: 7px 0 0 7px;
    color: var(--white); font-weight: 300; font-size: 15px; line-height: 21px;
    text-align: right; padding: 6px 32px 0 0;
  }

  .intro {
    position: absolute; left: 21px; top: 404px; width: 250px;
    color: var(--ink); font-size: 12.4px; line-height: 15.7px;
    text-align: justify; font-weight: 400;
  }
  .intro p + p { margin-top: 19px; }

  .services { position: absolute; left: 284px; top: 407px; width: 270px; }
  .services-title {
    font-family: "Montserrat", Arial, sans-serif; font-weight: 700;
    font-size: 19.5px; color: var(--navy); letter-spacing: .3px; margin-bottom: 9px;
  }
  .service-list { list-style: none; position: relative; }
  .service-list::before {
    content: ""; position: absolute; left: 5px; top: 8px; bottom: 8px;
    border-left: 2px dashed var(--teal);
  }
  .service-list li {
    position: relative; padding-left: 18px; color: var(--ink);
    font-size: 12.4px; line-height: 15.7px; margin-bottom: 11px;
  }
  .service-list li::before {
    content: ""; position: absolute; left: 0; top: 3px;
    width: 11px; height: 11px; border-radius: 50%; background: var(--teal);
  }

  .contact {
    position: absolute; left: 344px; top: 691px; width: 230px; height: 51px;
    border: 2px solid var(--teal); border-right: none; border-radius: 8px 0 0 8px;
    text-align: right; padding-right: 30px;
  }
  .contact-label {
    display: block; font-family: "Montserrat", Arial, sans-serif; font-weight: 700;
    font-size: 12px; color: var(--teal-text); letter-spacing: .5px; margin-top: 1px;
  }
  .contact-phone {
    display: inline-flex; align-items: center; gap: 8px;
    font-family: "Montserrat", Arial, sans-serif; font-weight: 700;
    font-size: 21px; color: var(--teal-text); margin-top: 2px;
  }
  .contact-phone svg { width: 22px; height: 22px; }

  .website {
    position: absolute; left: 0; right: 0; top: 758px; text-align: center;
    color: var(--teal-text); font-size: 15.5px; font-weight: 400;
  }
</style>
</head>
<body>
  <article class="flyer">
    <svg class="flyer-art" viewBox="0 0 566 800" width="566" height="800" aria-hidden="true">
      <defs>
        <linearGradient id="photoTone" x1="0" y1="0" x2="1" y2="1">
          <stop offset="0" stop-color="var(--photo-light)"/>
          <stop offset="1" stop-color="var(--photo-dark)"/>
        </linearGradient>
      </defs>
      <path class="swoosh" fill="var(--teal)"
        d="M0,148 C60,136 130,128 200,118 C260,110 288,94 322,96 C362,99 386,114 460,118 C520,122 566,126 566,126
           L566,340 C500,338 440,334 400,320 C352,302 300,318 230,330 C150,343 60,352 0,348 Z"/>
      <circle cx="161" cy="218" r="130" fill="var(--white)"/>
      <circle cx="161" cy="218" r="121" fill="var(--teal)"/>
    </svg>

    <svg class="flyer-art" viewBox="0 0 566 800" width="566" height="800" role="img"
         aria-label="Black and white photo of a smiling woman holding a calculator, framed in a circle">
      <path fill="url(#photoTone)" d="M118,60 C118,36 140,28 160,28 C182,28 204,36 204,60 L204,106
        A112 112 0 1 1 118,106 Z"/>
    </svg>

    <div class="brand">
      <span class="brand-mark"></span>
      Even Keel Ledger<br>Services
    </div>

    <h1 class="headline">
      <span class="headline-top">BOOKKEEPING</span>
      <span class="headline-main">TAILORED</span>
      <span class="headline-sub">TO YOUR BUSINESS NEEDS</span>
    </h1>

    <div class="credentials">
      Ledgerly Certified Advisor<br>Bookwise Pro Advisor
    </div>

    <div class="intro">
      <p>Are you a small business owner, tradie or PAVC Service Provider struggling to stay on top of your bookkeeping and compliance obligations? If so we would love to help you get back on track and take control of your business finances so that you can make informed business decisions and focus on what you do best.</p>
      <p>We have over 20 years industry experience and, as a small business ourselves, we are able to offer our clients a personal bookkeeping solution tailored to meet the needs of your business.</p>
    </div>

    <section class="services">
      <h2 class="services-title">SERVICES WE PROVIDE</h2>
      <ul class="service-list">
        <li>Accounts Payable | Accounts Receivable</li>
        <li>Customer Invoicing</li>
        <li>Bank and Credit Card Reconciliations</li>
        <li>Business Activity | Instalment Activity Statements</li>
        <li>Payroll | Superannuation | Payroll Tax</li>
        <li>Regular Financial Reports</li>
        <li>Ledgerly and Bookwise Set-Up and Training</li>
      </ul>
    </section>

    <div class="contact">
      <span class="contact-label">FOR MORE INFO</span>
      <span class="contact-phone">
        <svg viewBox="0 0 24 24" aria-hidden="true">
          <path fill="var(--teal)" d="M6.6 10.8c1.4 2.8 3.8 5.1 6.6 6.6l2.2-2.2c.3-.3.7-.4 1-.2 1.1.4 2.3.6 3.6.6.6 0 1 .4 1 1V20c0 .6-.4 1-1 1C10.6 21 3 13.4 3 4c0-.6.4-1 1-1h3.5c.6 0 1 .4 1 1 0 1.3.2 2.5.6 3.6.1.3 0 .7-.2 1z"/>
          <path fill="none" stroke="var(--teal)" stroke-width="1.8" stroke-linecap="round" d="M14.5 6.5a4 4 0 0 1 3 3M14.5 2.8a7.6 7.6 0 0 1 6.7 6.7"/>
        </svg>
        0400 187 352
      </span>
    </div>

    <div class="website">www.evenkeelledgerservices.com.au</div>
  </article>
</body>
</html>
```